Simple graphic for a book or slide presentation

We are looking for a style that suits the style of our book. It's title is Harbor. Keeping a calm course through stormy seas. There will be more line drawing/graphics in the book but how you design this image will create the style for all the other simple graphics in the book (once we decide what they are). So this one design will lead to a few more to match the style of this one. We'd like the shape of the overall graphic (i.e the arrows and words/bubbles) to be circular (not a rounded square as appears in the sample attached). Perhaps the words don't need to be in ovals or bound by anything at all; perhaps they do - let's see what you see. We'd like you to choose a font or offer many different fonts you think will capture the practical yet unconventional tone of the book. The book is teaching that managing risks in life is a life-skill that can be learned. The section of the book where this graphic will be placed is called "the power of language" - basically we are saying that thoughts, words and actions create our culture and our destiny. This insight comes from Torvel Pelloru's famous quote:
Carefully watch your thoughts, for they become your words.
Manage and watch your words, for they will become your actions.
Consider and judge your actions, for they have become your habits.
Acknowledge and watch your habits, for they shall become your values.
Understand and embrace your values, for they become your destiny.

Please change the text in the middle of the graphic to say: The Human Culture Cycle

```html
<!DOCTYPE html>
<html lang="en">
<head>
<meta charset="utf-8">
<title>The Human Culture Cycle</title>
<link rel="stylesheet" href="https://fonts.googleapis.com/css2?family=Figtree:wght@400;800&display=swap">
<style>
  :root {
    --paper: #ffffff;
    --ink: #000000;
    --thoughts: #ffec88;
    --words: #f7c97f;
    --actions: #f18cb8;
    --habits: #b491bf;
    --values: #98d3f0;
    --culture: #9ed39b;
  }
  html, body {
    margin: 0;
    padding: 0;
    width: 1200px;
    height: 1200px;
    overflow: hidden;
    background: var(--paper);
  }
  .cycle-diagram {
    display: block;
    width: 1200px;
    height: 1200px;
  }
  .segment--thoughts { fill: var(--thoughts); }
  .segment--words { fill: var(--words); }
  .segment--actions { fill: var(--actions); }
  .segment--habits { fill: var(--habits); }
  .segment--values { fill: var(--values); }
  .segment--culture { fill: var(--culture); }
  .hub { fill: var(--paper); }
  .stage-label {
    font-family: "Figtree", sans-serif;
    font-weight: 400;
    font-size: 84px;
    fill: var(--ink);
    text-anchor: middle;
  }
  .cycle-title {
    font-family: "Figtree", sans-serif;
    font-weight: 800;
    font-size: 80px;
    letter-spacing: 0.1em;
    fill: var(--ink);
    text-anchor: middle;
  }
</style>
</head>
<body>
<svg class="cycle-diagram" viewBox="0 0 1932 1932" role="img" aria-label="The Human Culture Cycle: Thoughts, Words, Actions, Habits, Values, Culture">
  <g class="ring">
    <path class="segment segment--thoughts" d="M584,320 A750,750 0 0 1 1334,313 L1266,434 L1332,547 L1200,549 L1132,670 A339,339 0 0 0 793,674 L722,554 L787,439 L654,440 Z"/>
    <path class="segment segment--words" d="M1334,313 A750,750 0 0 1 1716,958 L1576,960 L1511,1075 L1443,961 L1304,962 A339,339 0 0 0 1132,670 L1200,549 L1332,547 L1266,434 Z"/>
    <path class="segment segment--actions" d="M1716,958 A750,750 0 0 1 1348,1611 L1278,1492 L1144,1492 L1209,1377 L1139,1257 A339,339 0 0 0 1304,962 L1443,961 L1511,1075 L1576,960 Z"/>
    <path class="segment segment--habits" d="M1348,1611 A750,750 0 0 1 598,1619 L665,1498 L599,1384 L732,1383 L800,1261 A339,339 0 0 0 1139,1257 L1209,1377 L1144,1492 L1278,1492 Z"/>
    <path class="segment segment--values" d="M598,1619 A750,750 0 0 1 216,973 L355,972 L420,857 L487,970 L627,969 A339,339 0 0 0 800,1261 L732,1383 L599,1384 L665,1498 Z"/>
    <path class="segment segment--culture" d="M216,973 A750,750 0 0 1 584,320 L654,440 L787,439 L722,554 L793,674 A339,339 0 0 0 627,969 L487,970 L420,857 L355,972 Z"/>
  </g>
  <circle class="hub" cx="966" cy="966" r="336"/>
  <g class="stage-labels">
    <text class="stage-label" x="981" y="457">Thoughts</text>
    <text class="stage-label" x="1417" y="718">Words</text>
    <text class="stage-label" x="1441" y="1244">Actions</text>
    <text class="stage-label" x="983" y="1535">Habits</text>
    <text class="stage-label" x="479" y="1244">Values</text>
    <text class="stage-label" x="498" y="718">Culture</text>
  </g>
  <text class="cycle-title">
    <tspan x="970" y="855">THE</tspan>
    <tspan x="970" y="940">HUMAN</tspan>
    <tspan x="970" y="1024">CULTURE</tspan>
    <tspan x="970" y="1108">CYCLE</tspan>
  </text>
</svg>
</body>
</html>
```